Business Card design for an International Import Export House

We need a Business Card design for our import export business. We trade in Minerals, Metals, Rice, Sugar, Steel etc.. The design should be minimalistic. It may or may not contain the physical address. In case you want to include the physical address - 418 Verandah Heights, Marlow Sector 9, Gurgaon, Haryana, India, 122009.

Target Market(s)

Steel Mills or Steel Plants, Factories, Mining businesses, Industrial houses, Government Agencies

Industry/Entity Type

Importer

Contact Information for Business Card

Business Name - Tessan Overseas

Font styles to use
Other font styles liked:
• montserrat

Requirements
Must have
• Ravi Kandola - President
• www.tessanoverseas.com
• ravi@tessanoverseas.com
• +91-987-654-3217
Nice to have
• worldwide suppliers of ores

```html
<!DOCTYPE html>
<html lang="en">
<head>
<meta charset="utf-8">
<title>Tessan Overseas – Business Card</title>
<link rel="stylesheet" href="https://fonts.googleapis.com/css2?family=Montserrat:wght@400;500;600;700&display=swap">
<style>
  :root {
    --teal: #3f8ca6;
    --ink: #1b1f22;
    --card-dark: #1a1d20;
    --paper: #ffffff;
    --stage: #e9e7e4;
    --light-text: #f2f4f5;
  }
  * { box-sizing: border-box; margin: 0; padding: 0; }
  html, body {
    width: 1200px; height: 843px; overflow: hidden;
    background: var(--stage);
    font-family: "Montserrat", sans-serif;
  }
  .canvas { position: relative; width: 1200px; height: 843px; }
  .card {
    position: absolute; top: 252px; width: 558px; height: 319px;
    border-radius: 13px;
    box-shadow: 0 3px 8px rgba(0,0,0,0.25);
    overflow: hidden;
  }
  .card--front { left: 28px; background: var(--paper); color: var(--ink); }
  .card--back { left: 615px; background: var(--card-dark); }

  .contact { position: absolute; left: 23px; top: 87px; }
  .contact__name {
    font-size: 20px; font-weight: 700; letter-spacing: 0.6px;
    text-transform: uppercase; line-height: 1;
  }
  .contact__name .first { color: var(--teal); }
  .contact__role { color: var(--teal); font-size: 14px; margin-top: 5px; line-height: 1.2; }
  .contact__address { font-size: 14.2px; line-height: 18.5px; margin-top: 6px; }
  .contact__lines { list-style: none; margin-top: 4px; font-size: 14.2px; }
  .contact__lines li { display: flex; align-items: center; height: 18.5px; }
  .contact__lines svg { width: 9px; height: 9px; margin-right: 5px; fill: var(--teal); flex: none; }
  .contact__lines .accent { color: var(--teal); }

  .brand {
    position: absolute; right: 34px; top: 310px; transform: translateY(-100%);
    display: flex; align-items: center; gap: 10px;
    position: absolute;
  }
  .brand__dot { width: 16px; height: 16px; border-radius: 50%; background: var(--teal); }
  .brand__name {
    color: var(--teal); font-size: 21px; font-weight: 700;
    letter-spacing: -0.3px; text-transform: uppercase;
  }
  .card--back .brand { top: auto; bottom: 78px; transform: none; }
</style>
</head>
<body>
<main class="canvas">
  <section class="card card--front" aria-label="Card front">
    <div class="contact">
      <h1 class="contact__name"><span class="first">Ravi</span> Kandola</h1>
      <p class="contact__role">President</p>
      <p class="contact__address">418 Verandah Heights, Marlow Sector 9<br>Gurgaon, Haryana, India, 122009</p>
      <ul class="contact__lines">
        <li><svg viewBox="0 0 10 10" aria-hidden="true"><path d="M2 0.5 L3.6 0.5 L4 3 L3 3.8 Q3.8 5.6 5.4 6.8 L6.3 5.9 L8.8 6.4 L8.8 8.2 Q8.6 9.5 7 9.4 Q1 8.6 0.7 2 Q0.7 0.6 2 0.5Z"/></svg>+91-987-654-3217</li>
        <li><svg viewBox="0 0 10 10" aria-hidden="true"><path d="M0 2 L5 5.6 L10 2 L10 8.5 L0 8.5Z M0.4 1.5 L9.6 1.5 L5 4.8Z"/></svg>ravi@tessanoverseas.com</li>
        <li><svg viewBox="0 0 10 10" aria-hidden="true"><circle cx="5" cy="5" r="4.3" fill="none" stroke="#3f8ca6" stroke-width="0.9"/><ellipse cx="5" cy="5" rx="1.9" ry="4.3" fill="none" stroke="#3f8ca6" stroke-width="0.8"/><path d="M0.7 5 H9.3 M1.4 2.9 H8.6 M1.4 7.1 H8.6" stroke="#3f8ca6" stroke-width="0.7"/></svg>www.<span class="accent">tessanoverseas</span>.com</li>
      </ul>
    </div>
  </section>

  <section class="card card--back" aria-label="Card back">
    <div class="brand">
      <span class="brand__dot" aria-hidden="true"></span>
      <span class="brand__name">Tessan Overseas</span>
    </div>
  </section>
</main>
</body>
</html>
```